Home page improvements

We're looking for a designer to make changes to the home page of our site www.mendlark.com to:
a) include space for a featured article or blog
b) reduce the size of the ad and to create more ads for rotation
c) include space for special offers (2-3 featured repairs) - these can be links to the detailed repair page.
We're not looking for substantial redesign. We will have other design tasks on an ongoing basis for the winning designer, so an indication of hourly charge-out rate would be appreciated.
You're welcome to submit other changes you feel would benefit the site also.
Look and feel
Each slider illustrates characteristics of the customer's brand and the style your logo design should communicate.

```html
<!DOCTYPE html>
<html lang="en">
<head>
<meta charset="utf-8">
<title>Mendlark – Home</title>
<link rel="stylesheet" href="https://fonts.googleapis.com/css2?family=Arimo:wght@400;700&family=Open+Sans:wght@400;600&family=Noto+Sans:wght@400&family=Noto+Serif&family=Anton&display=swap">
<style>
:root{
  --page:#ececec;--band:#f4f4f4;--band-dark:#e6e6e6;--ink:#222;--ink-soft:#555;--muted:#888;
  --brand:#4aa3df;--brand-dark:#2f83c3;--navy:#182a5e;--yellow:#f7d316;--red:#e42a2a;--pink:#df6fa6;--teal:#1d9a8a;--line:#cfcfcf;
}
*{margin:0;padding:0;box-sizing:border-box}
html,body{width:918px;height:1200px;overflow:hidden}
body{position:relative;background:var(--page);font-family:Arimo,Arial,sans-serif;color:var(--ink)}
.abs{position:absolute}
.top-rule{left:0;top:10px;width:918px;height:1px;background:#999}
.locale{left:86px;top:21px;font-size:9px;font-weight:700;color:#333}
.ad-banner{left:354px;top:22px;width:518px;height:52px;background:#fff;overflow:hidden}
.ad-banner span{position:absolute;left:40px;top:6px;font-family:"Noto Serif",serif;font-size:19px;color:var(--teal);letter-spacing:.5px}
.ad-banner .ad-art{position:absolute;right:0;top:0;width:80px;height:52px;background:radial-gradient(circle at 70% 60%,#fff 0 18%,#2a9bd0 30%,#19a36f 55%,#fff 80%)}
.brand{display:flex;align-items:center;gap:12px}
.brand-name{font-family:Arimo,Arial,sans-serif;font-weight:700;color:#444;letter-spacing:-1px;white-space:nowrap}
.brand-mark{background:var(--brand);border-radius:4px;flex:none}
.site-brand{left:90px;top:72px}
.site-brand .brand-name{font-size:44px}
.site-brand .brand-mark{width:48px;height:48px}
.util-nav{right:54px;top:96px;display:flex;font-size:10px;color:#222}
.util-nav a{padding:0 8px;border-left:1px solid #999;color:inherit;text-decoration:none;line-height:11px}
.util-nav a:first-child{border-left:0}
.util-nav a:last-child{padding-right:0}
.main-nav{right:66px;top:123px;display:flex;gap:28px;font-size:12px;font-weight:600;font-family:"Open Sans",sans-serif;white-space:nowrap}
.hero{left:76px;top:162px;width:783px;height:222px;border-radius:6px;background:radial-gradient(circle at 30% 20%,#f6f1f0,#e2dbda 60%,#d7d0cf);box-shadow:0 2px 4px rgba(0,0,0,.35);overflow:hidden}
.hero-device{position:absolute;left:19px;top:6px;width:108px;height:210px;border-radius:16px;background:linear-gradient(160deg,#333,#111 40%,#3a6fb0 55%,#111 90%)}
.hero-title{position:absolute;font-family:"Noto Sans",sans-serif;font-size:46px;color:#111;line-height:1;white-space:nowrap}
.hero-sub{position:absolute;left:143px;top:152px;font-family:"Noto Sans",sans-serif;font-size:15.5px;color:#666;white-space:nowrap}
.btn{display:block;background:linear-gradient(#6cc0f2,#3b98d8 55%,#2b86c8);border-radius:5px;color:#fff;text-align:center;text-decoration:none;box-shadow:0 1px 2px rgba(0,0,0,.3)}
.btn strong{display:block;font-weight:700;letter-spacing:.5px}
.btn small{display:block;font-size:9px;color:#123}
.hero-cta{position:absolute;left:565px;top:78px;width:190px;height:62px;padding-top:10px}
.hero-cta strong{font-size:25px;line-height:25px}
.hero-more{position:absolute;left:565px;top:142px;font-size:15px;color:#777;display:flex;align-items:center;gap:6px;font-family:"Open Sans",sans-serif}
.tour-tag{font-size:6px;font-weight:700;color:#fff;background:#666;padding:2px 12px 2px 8px;clip-path:polygon(0 0,88% 0,100% 50%,88% 100%,0 100%);letter-spacing:.5px}
.feature-band{left:0;top:398px;width:918px;height:229px;background:var(--band)}
.blog-icon{left:97px;top:430px;width:46px;height:46px;border-radius:50%;background:radial-gradient(circle at 40% 35%,#6fb8ea,#1f6eb3)}
.blog-head{left:153px;top:452px;font-family:"Open Sans",sans-serif;font-size:14px;color:#333}
.blog-body{left:109px;top:489px;width:200px;font-size:10px;line-height:12px;color:#223}
.blog-body p+p{margin-top:11px}
.blog-rule{left:86px;top:604px;width:247px;height:4px;background:var(--brand-dark)}
.offer{left:345px;top:400px;width:247px;height:205px;background:var(--navy);overflow:hidden;text-align:center}
.offer:before{content:"";position:absolute;left:110px;top:-40px;width:260px;height:320px;border-radius:50%;background:#2c4f98}
.offer>*{position:relative}
.offer-kicker{margin-top:28px;font-family:Anton,sans-serif;font-size:23px;color:var(--yellow);letter-spacing:.5px}
.offer-pct{margin-top:8px;font-family:Anton,sans-serif;font-size:34px;color:var(--red);-webkit-text-stroke:1px #fff}
.offer-line{margin-top:8px;font-size:10.5px;color:#fff}
.offer-burst{position:absolute;left:72px;top:154px;width:116px;height:70px;border-radius:50%;background:var(--yellow);padding-top:22px;font-size:11px;color:#222}
.promo-art{left:604px;top:400px;width:248px;height:205px;background:radial-gradient(circle at 45% 50%,#e782b3,#d85f9c)}
.info-band{left:0;top:627px;width:918px;height:91px;background:var(--band-dark)}
.info{top:640px;width:190px}
.info h2,.card h2{font-family:"Open Sans",sans-serif;font-weight:400;font-size:15px;color:#222;white-space:nowrap}
.info p{margin-top:10px;font-size:9.5px;line-height:12px;color:#222}
.card-img{top:758px;width:222px;height:163px;border-radius:6px;box-shadow:0 1px 3px rgba(0,0,0,.35);overflow:hidden}
.map{left:77px;background:linear-gradient(135deg,#c9c7bf,#dedcd4 50%,#b9b6ad)}
.timer{position:absolute;right:-4px;bottom:-6px;width:80px;height:80px;border-radius:50%;background:var(--red);color:#fff;text-align:center;padding-top:14px;font-size:6px;font-weight:700}
.timer b{display:block;font-family:Anton,sans-serif;font-size:34px;line-height:38px;font-weight:400}
.plane{left:357px;background:linear-gradient(#5e8fd0,#a9c8ea 55%,#e8eef6)}
.ribbon{position:absolute;left:-22px;top:22px;width:110px;transform:rotate(-45deg);background:#3aa39a;color:#fff;font-size:8px;font-weight:700;text-align:center;padding:3px 0}
.compare{left:637px;background:#fff;font-size:7px;color:#333}
.compare h3{font-family:"Open Sans",sans-serif;font-weight:400;font-size:13px;padding:12px 0 0 15px;white-space:nowrap}
.compare p{padding:4px 0 0 15px;white-space:nowrap;font-size:7px;color:#555}
.compare table{position:absolute;left:10px;top:58px;border-collapse:collapse;width:230px}
.compare td{border:1px solid #ccc;height:25px;padding:0 6px;font-size:6.5px}
.compare th{font-weight:400;font-size:9px;height:18px;text-align:center}
.compare td+td{text-align:center;width:76px;background:#fafafa}
.card{top:934px;width:240px}
.card h3{font-family:"Open Sans",sans-serif;font-weight:400;font-size:13.5px;color:#888;white-space:nowrap}
.card p{margin-top:8px;width:195px;font-size:9px;line-height:12px;color:#777}
.card a{color:var(--brand-dark);text-decoration:none;font-weight:700}
.footer{left:0;top:1042px;width:918px;height:148px;background:#f1f1f1}
.foot-brand{left:75px;top:1078px}
.foot-brand .brand-name{font-size:38px}
.foot-brand .brand-mark{width:40px;height:40px}
.foot-col{top:1068px;font-size:9.5px;line-height:15px;color:#222}
.foot-col h4{font-family:"Open Sans",sans-serif;font-weight:400;font-size:14px;color:#7db4db;margin-bottom:4px}
.foot-cta{left:581px;top:1070px;width:264px;height:60px;padding-top:12px}
.foot-cta strong{font-size:24px;line-height:24px}
.foot-rule{left:75px;top:1157px;width:789px;height:1px;background:#666}
.legal{left:77px;top:1172px;font-size:9px;display:flex;align-items:center}
.legal b{margin-right:42px}
.legal a{color:var(--brand-dark);text-decoration:none;padding:0 14px;border-left:1px solid #999}
.legal a:first-of-type{border-left:0}
.pay{left:735px;top:1165px;display:flex;gap:6px}
.pay span{width:30px;height:20px;border:1px solid #bbb;border-radius:2px}
</style>
</head>
<body>
<div class="abs top-rule"></div>
<div class="abs locale">Location United States</div>
<div class="abs ad-banner"><span>AD BANNER SPACE</span><div class="ad-art" role="img" aria-label="Abstract colourful advert artwork"></div></div>

<div class="abs brand site-brand"><span class="brand-name">mendlark</span><span class="brand-mark"></span></div>
<nav class="abs util-nav"><a href="#">Find us</a><a href="#">About us</a><a href="#">Contact us</a><a href="#">Customer login</a></nav>
<nav class="abs main-nav"><span>Repairs &amp; pricing</span><span>Tour</span><span>Why choose us</span><span>FAQ</span><span>Blog</span></nav>

<section class="abs hero">
  <div class="hero-device" role="img" aria-label="Photo of a smartphone being repaired, split into pieces"></div>
  <div class="hero-title" style="left:144px;top:38px">10,000 repairs</div>
  <div class="hero-title" style="left:209px;top:96px">and counting.</div>
  <div class="hero-sub">When it comes to experience, no one else comes close.</div>
  <a class="btn hero-cta" href="#"><strong>REPAIRS</strong><small>NO PAYMENT UNTIL IT'S FIXED</small></a>
  <div class="hero-more">or LEARN MORE <span class="tour-tag">TAKE THE TOUR</span></div>
</section>

<div class="abs feature-band"></div>
<div class="abs blog-icon"></div>
<div class="abs blog-head">Recent blog post</div>
<div class="abs blog-body"><p>Playing with Location based Reminders</p><p>One of the many new features that come with the LumoOS 5 upgrade is the new Reminders app. My first thought was “why do I need another productivity app?”.</p></div>
<div class="abs blog-rule"></div>

<div class="abs offer">
  <div class="offer-kicker">SPECIAL OFFER</div>
  <div class="offer-pct">40% off</div>
  <div class="offer-line">ON ALL REPAIRS THIS FESTIVE SEASON</div>
  <div class="offer-burst">find out more</div>
</div>
<div class="abs promo-art" role="img" aria-label="Advert: silhouette of a dancer listening to a music player on a pink background"></div>

<div class="abs info-band"></div>
<div class="abs info" style="left:86px"><h2>What do we fix?</h2><p>Lumo phones and Lumo players, from broken screens to headphone jacks to home keys and everything else in between.</p></div>
<div class="abs info" style="left:366px"><h2>Who is it for?</h2><p>Anyone who wants the best quality repair at affordable prices. Whether you're in New York, LA or the mountains of Alaska.</p></div>
<div class="abs info" style="left:646px"><h2>Why repair?</h2><p>The same quality as a brand new phone. By the the most experienced and trusted phone and player repair service.</p></div>

<div class="abs card-img map" role="img" aria-label="Street map of SoHo, New York with a location pin">
  <div class="timer">FIXED IN<b>30</b>MINUTES</div>
</div>
<div class="abs card-img plane" role="img" aria-label="Photo of a Skyfreight cargo plane above the clouds">
  <div class="ribbon">FREE SHIPPING</div>
</div>
<div class="abs card-img compare">
  <h3>There's Mendlark. And then there's</h3>
  <p>If you rely on your phone and can't live without it, Mendlark is t</p>
  <table>
    <tr><th></th><th>Mendlark</th></tr>
    <tr><td>Just rock up, fixed on-the-spot</td><td><svg width="14" height="12" viewBox="0 0 14 12"><path d="M1 6l4 4 8-9" fill="none" stroke="#3aa33a" stroke-width="2.5"/></svg></td></tr>
    <tr><td>Instant status updates</td><td>SMS &amp; Email</td></tr>
    <tr><td>Genuine parts only</td><td>Yes</td></tr>
  </table>
</div>

<div class="abs card" style="left:86px"><h2>In New York City?</h2><h3>Visit our workshop SoHo.</h3><p>If it just can't wait, drop in and we'll fix your device on the spot! Conveniently located for ultimate convenience. <a href="#">Find us ›</a></p></div>
<div class="abs card" style="left:366px"><h2>Premium mail-in service.</h2><h3>Back in a flash - 24 hour turnaround.</h3><p>All repairs shipped out same day as they arrive. Best of all return shipping is free!<br><a href="#">Learn more ›</a></p></div>
<div class="abs card" style="left:646px"><h2>Better in every way</h2><h3>There's no comparison.</h3><p>We're focussed on providing the highest quality repairs and the best repair service guaranteed. <a href="#">Learn more ›</a></p></div>

<footer>
  <div class="abs footer"></div>
  <div class="abs brand foot-brand"><span class="brand-name">mendlark</span><span class="brand-mark"></span></div>
  <div class="abs foot-col" style="left:308px"><h4>More info</h4>Shipping policy<br>Warranty policy<br>Terms &amp; conditions</div>
  <div class="abs foot-col" style="left:396px"><h4>About us</h4>Our story<br>Guarantee<br>Careers</div>
  <div class="abs foot-col" style="left:466px"><h4>Questions?</h4>FAQ<br>Contact us<br>Take the tour</div>
  <a class="abs btn foot-cta" href="#"><strong>REPAIRS &amp; PRICING</strong><small>CLICK HERE TO GET STARTED</small></a>
  <div class="abs foot-rule"></div>
  <div class="abs legal"><b>© 2011 Mendlark LLC</b><a href="#">Legal</a><a href="#">Privacy Policy</a></div>
  <div class="abs pay"><span style="background:#fff"></span><span style="background:#f3b13a"></span><span style="background:#fff"></span><span style="background:#5a8fd0"></span></div>
</footer>
</body>
</html>
```